Packaging Design for Snack Food Company

Our company is Crumble Hollow (www.crumblehollow.com.au). We import and manufacturer a range of snack foods which are sold throughout Australia.

Our range of snacks can be viewed at www.crumblehollow.com.au. Currently we use a plain bag with a label but we want to move to a bag with a graphic design.

We have a few basic requirements.
1. Bag material is 50um polypropylene.
2. Bag size is 475mm width x 350mm length (see attached photo of drawing for more info).
3. We want a clear window on the front and back of the bag.
4. Front side must have our logo (see attached image). We are open to a new logo design if you can think of something better than our current one.
5. Back side must have space (85mm x 60mm) for printing ingredients, nutritional information, bar code & expiry date and have our address & contact information.
6. Top and bottom of the bag must be opaque to hide the product, the window can be positioned somewhere in the centre of the bag.
7. We want to use only one bag across our range of snacks. Our packing machine will print on the front side clear window what each product is ie. Cracker Mix Nacho Cheese 160g and on the back it will print the ingredients and nutritional info etc.

Our logo is in the files below along with some design ideas.

UPDATE 3/8/16
Some great designs have been submitted so far. Thank you. We have now
guaranteed the projected so we are committed to purchasing a design.

Industry/Entity Type

It Company

Requirements
Must have
• No must haves, we are open to any design ideas.

```html
<!DOCTYPE html>
<html lang="en">
<head>
<meta charset="utf-8">
<title>Crumble Hollow – Snack Bag Artwork</title>
<link href="https://fonts.googleapis.com/css2?family=Arimo:wght@400;700&family=Dancing+Script:wght@600&display=swap" rel="stylesheet">
<style>
  :root {
    --stage: #dcdcdc;
    --cream: #fbf3d2;
    --brand-blue: #2b64b4;
    --brand-red: #e2392b;
    --ink: #1d1d1d;
    --label-white: #ffffff;
    --snack-light: #f4c25a;
    --snack-deep: #c98a2a;
  }
  * { box-sizing: border-box; margin: 0; padding: 0; }
  html, body {
    width: 1200px; height: 612px; overflow: hidden;
    background: var(--stage);
    font-family: "Arimo", Arial, sans-serif;
  }
  .bag-artwork {
    position: absolute; left: 225px; top: 26px;
    width: 750px; height: 560px;
    background: var(--cream);
    overflow: hidden;
  }
  .artwork-shapes { position: absolute; inset: 0; }
  .wordmark {
    position: absolute;
    font-weight: 700; color: var(--brand-red);
    text-align: center; line-height: 1.05;
  }
  .wordmark--back { left: 34px; top: 92px; width: 120px; font-size: 20px; }
  .wordmark--front { left: 305px; top: 96px; width: 170px; font-size: 24px; }
  .company-details {
    position: absolute; left: 26px; top: 200px; width: 134px;
    text-align: center; color: var(--brand-blue);
    font-style: normal;
    font-size: 8.4px; font-weight: 700; line-height: 1.3;
  }
  .company-details .company-name { font-size: 9.5px; }
  .info-panel {
    position: absolute; left: 33px; top: 258px;
    width: 133px; height: 193px;
    background: var(--label-white);
    padding: 6px 7px; color: var(--ink);
  }
  .nutrition-table {
    width: 100%; border: 0.8px solid var(--ink);
    border-collapse: collapse; font-size: 4.6px; line-height: 1.25;
  }
  .nutrition-table caption {
    caption-side: top; text-align: left; font-weight: 700;
    font-size: 5.6px; border: 0.8px solid var(--ink); border-bottom: 0;
    padding: 1px 2px;
  }
  .nutrition-table .serving-note { font-weight: 400; font-size: 4.4px; display: block; }
  .nutrition-table th, .nutrition-table td { padding: 0.5px 2px; text-align: left; }
  .nutrition-table th { font-weight: 700; border-bottom: 0.6px solid var(--ink); }
  .nutrition-table td:not(:first-child), .nutrition-table th:not(:first-child) { text-align: right; }
  .best-before { font-weight: 700; font-size: 8.5px; margin: 5px 0 4px; }
  .ingredients, .allergens { font-size: 4.6px; line-height: 1.35; }
  .allergens { margin-top: 5px; }
  .disposal-note {
    position: absolute; left: 33px; top: 466px;
    width: 133px; height: 32px;
    border: 1.2px solid var(--brand-blue); border-radius: 3px;
    display: flex; align-items: center; gap: 6px; padding: 0 5px;
    color: var(--brand-blue); font-size: 7.4px; font-weight: 700; line-height: 1.2;
  }
  .disposal-note svg { flex: none; border-right: 1.2px solid var(--brand-blue); padding-right: 4px; }
  .tagline {
    position: absolute; left: 152px; top: 350px; width: 160px; height: 30px;
    font-family: "Dancing Script", cursive; font-size: 23px; line-height: 30px;
    color: var(--label-white); text-align: center; white-space: nowrap;
    transform: rotate(-80deg);
  }
</style>
</head>
<body>
<main class="bag-artwork">
  <svg class="artwork-shapes" width="750" height="560" viewBox="0 0 750 560">
    <defs>
      <radialGradient id="snackFill" cx="50%" cy="50%" r="60%">
        <stop offset="0" stop-color="var(--snack-light)"/>
        <stop offset="1" stop-color="var(--snack-deep)"/>
      </radialGradient>
    </defs>
    <path class="brand-band"
          d="M268 48 C 215 150, 192 300, 212 400 C 232 480, 300 530, 345 560 L 390 560 C 330 520, 272 470, 256 400 C 240 300, 255 160, 302 52 Z"
          fill="var(--brand-blue)"/>
    <g class="product-window" role="img" aria-label="Clear window showing the snack chips inside the bag">
      <path d="M365 552 C 300 480, 272 380, 292 290 C 307 215, 360 172, 420 176 C 480 180, 520 230, 530 285 C 560 240, 620 225, 665 245 C 712 266, 716 332, 690 382 C 640 462, 500 520, 365 552 Z"
            fill="url(#snackFill)" stroke="var(--brand-red)" stroke-width="5"/>
    </g>
  </svg>

  <p class="wordmark wordmark--back">Crumble<br>Hollow</p>

  <address class="company-details">
    <span class="company-name">Crumble Hollow Pty Ltd</span><br>
    27 Millbrook Lane<br>
    Brookvale, VIC 3099<br>
    Phone: 03 9000 1234<br>
    www.crumblehollow.com.au
  </address>

  <section class="info-panel">
    <table class="nutrition-table">
      <caption>Nutritional Information<span class="serving-note">Servings per pack: 4 Serving size: 40g</span></caption>
      <thead><tr><th></th><th>Per Serve</th><th>Per 100g</th></tr></thead>
      <tbody>
        <tr><td>Energy</td><td>820kJ</td><td>2050kJ</td></tr>
        <tr><td>Protein</td><td>2.4g</td><td>6.0g</td></tr>
        <tr><td>Fat, total</td><td>9.6g</td><td>24g</td></tr>
        <tr><td>Saturated</td><td>1.2g</td><td>3.0g</td></tr>
        <tr><td>Carbohydrate</td><td>22g</td><td>55g</td></tr>
        <tr><td>Sugars</td><td>0.8g</td><td>2.0g</td></tr>
        <tr><td>Sodium</td><td>240mg</td><td>600mg</td></tr>
      </tbody>
    </table>
    <p class="best-before">Best Before: 23 07 16</p>
    <p class="ingredients">Ingredients: Corn, Vegetable Oil, Rice Flour, Salt, Cheese Powder, Onion, Garlic, Paprika, Yeast Extract, Spices.</p>
    <p class="allergens">Contains milk. Made on shared lines.</p>
  </section>

  <div class="disposal-note">
    <svg width="22" height="20" viewBox="0 0 22 20" aria-hidden="true">
      <path d="M4 6 H14 L13 18 H5 Z M3 5 H15" fill="none" stroke="var(--brand-blue)" stroke-width="1.6"/>
      <circle cx="15" cy="2.5" r="1.6" fill="var(--brand-blue)"/>
    </svg>
    <span>Please dispose of this product thoughtfully</span>
  </div>

  <p class="tagline">Quality Snacks</p>
  <p class="wordmark wordmark--front">Crumble<br>Hollow</p>
</main>
</body>
</html>
```